Design A Printed Box in .AI For A DNA Test Kit

Greetings freelancers!

We are a company that uses your DNA to help you find the right cannabis products.

We are currently looking for someone to design the boxes that we will be using to send consumers their DNA test kit.

I have attached the box design that we have been asked to provide to the logistics company.

There are several things we would like to have done here:

Outer side:

1) Replace text on the back that currently starts with "Thank you for choosing Veltrisyn..." with the copy and formatting in the attached word document: Back Cover Copy Cobalt Wren Test Kit

2) Remove the Veltrisyn Buccal Collection Kit from the Side Panel and replace with the cobalt wren logo, but move the words "Cobalt Wren" to the right of the logo and put "Buccal Collection Kit" centered below the image/words. Do the same for the other side, making sure that it is rotated to account for the box.

3) Replace the BUCCAL COLLECTION KIT Veltrisyn on the top flap outer side with the cobalt wren logo centered and some minimal background design that uses DNA and cannabis leaves in a tasteful manner. I have included a "Cobalt Wren Inspiration" image that references how I'd like it to look, generally, but instead of just geometries, using DNA / cannabis leaves outlines. We have a really minimal design style that we are going for, so please be mindful of that.

Inner Side:

4) On the inner side, please replace the copy with that included in "Cobalt Wren Inside Cover Copy"

5) Continue the cannabis / DNA minimal design that was used in #4 as accents throughout the rest of the box, so that there is something on each side, but still very minimal. This should be seen throughout the box design.

PLEASE USE THE INCLUDED FONT STYLES included as a .zip.

Please submit your entry via a .jpeg output of the images. I cannot easily view .AI files.

```html
<!DOCTYPE html>
<html lang="en">
<head>
<meta charset="utf-8">
<title>Cobalt Wren – Buccal Collection Kit Box Dieline</title>
<link href="https://fonts.googleapis.com/css2?family=Montserrat:wght@400;600&family=Noto+Sans+KR:wght@400&display=swap" rel="stylesheet">
<style>
  :root{
    --paper:#ffffff;
    --die:#e887cf;
    --label:#e04fb8;
    --ink:#333a40;
    --brand:#2f7fb5;
    --net-blue:#4f8fd0;
    --net-green:#8fcc5c;
    --step-fill:#eef1f4;
    --alert:#e23b5a;
  }
  html,body{margin:0;padding:0;overflow:hidden;background:var(--paper);}
  .sheet{display:block;width:1200px;height:848px;}
  .die{fill:none;stroke:var(--die);stroke-width:.9;}
  .side-label{font-family:"Noto Sans KR",sans-serif;font-size:8px;fill:var(--label);}
  .brand-name{font-family:"Montserrat",sans-serif;font-weight:600;fill:var(--brand);letter-spacing:1px;}
  .brand-dot{fill:var(--brand);}
  .small-copy{font-family:"Montserrat",sans-serif;font-weight:400;fill:var(--ink);}
  .strong{font-weight:600;}
  .step-art{fill:var(--step-fill);stroke:#c9d0d6;stroke-width:.4;}
  .bullet{fill:var(--alert);}
</style>
</head>
<body>
<svg class="sheet" viewBox="0 0 900 636" xmlns="http://www.w3.org/2000/svg">
  <defs>
    <linearGradient id="net-band" x1="0" y1="0" x2="1" y2="0">
      <stop offset="0" stop-color="#4f8fd0" stop-opacity=".45"/>
      <stop offset=".5" stop-color="#8fcc5c" stop-opacity=".4"/>
      <stop offset="1" stop-color="#4f8fd0" stop-opacity=".3"/>
    </linearGradient>
    <linearGradient id="net-band-fade" x1="0" y1="0" x2="1" y2="1">
      <stop offset="0" stop-color="#8fcc5c" stop-opacity=".35"/>
      <stop offset=".5" stop-color="#4f8fd0" stop-opacity=".25"/>
      <stop offset="1" stop-color="#4f8fd0" stop-opacity=".05"/>
    </linearGradient>
    <linearGradient id="net-faint" x1="0" y1="0" x2="1" y2="1">
      <stop offset="0" stop-color="#4f8fd0" stop-opacity=".22"/>
      <stop offset=".5" stop-color="#8fcc5c" stop-opacity=".16"/>
      <stop offset="1" stop-color="#4f8fd0" stop-opacity=".1"/>
    </linearGradient>
    <radialGradient id="net-dense" cx=".45" cy=".6" r=".6">
      <stop offset="0" stop-color="#2f6fb5" stop-opacity=".6"/>
      <stop offset=".7" stop-color="#4f8fd0" stop-opacity=".3"/>
      <stop offset="1" stop-color="#4f8fd0" stop-opacity="0"/>
    </radialGradient>
  </defs>

  <text class="side-label" x="245" y="77" text-anchor="middle">&lt; 바깥면_Outer side &gt;</text>
  <text class="side-label" x="690" y="77" text-anchor="middle">&lt; 안쪽면_inner side &gt;</text>

  <!-- ================= OUTER SIDE ================= -->
  <g class="outer-side">
    <g class="network-accents">
      <path d="M100 112 H260 L230 130 L150 140 L112 160 L100 150 Z" fill="url(#net-band)" role="img" aria-label="Blue and green polygon network along the top left of the lid"/>
      <path d="M120 245 L190 225 L260 205 L330 190 L400 178 V225 L330 230 L250 240 L170 250 Z" fill="url(#net-band)" role="img" aria-label="Blue and green polygon network rising across the lower lid"/>
      <rect x="105" y="262" width="270" height="108" fill="url(#net-faint)" role="img" aria-label="Faint polygon network across the back panel"/>
      <path d="M105 370 L140 370 L200 378 L170 395 L105 400 Z" fill="url(#net-band-fade)" role="img" aria-label="Polygon network trailing into the lower tuck panel"/>
      <path d="M78 430 L150 440 L190 470 L180 512 L78 512 Z" fill="url(#net-dense)" role="img" aria-label="Dense blue polygon network in the lower left of the front panel"/>
      <path d="M290 470 L350 450 L400 445 V512 L300 512 Z" fill="url(#net-dense)" role="img" aria-label="Dense blue polygon network in the lower right of the front panel"/>
      <path d="M290 420 L340 415 L345 440 L300 460 Z" fill="url(#net-band-fade)" role="img" aria-label="Scattered light blue triangles beside the brand name"/>
    </g>

    <g class="die">
      <path d="M95 88 H380 L400 96 V110 H75 V96 Z"/>
      <rect x="75" y="110" width="325" height="115"/>
      <rect x="130" y="130" width="220" height="58" rx="6"/>
      <path d="M55 225 H420 V260 H55 Z"/>
      <path d="M75 225 V260 M400 225 V260"/>
      <rect x="65" y="260" width="330" height="110"/>
      <path d="M105 260 V370 M375 260 V370"/>
      <path d="M65 270 H32 V360 H65"/>
      <path d="M395 270 H428 V360 H395"/>
      <path d="M55 370 H420 V405 H55 Z"/>
      <path d="M75 370 V405 M400 370 V405"/>
      <path d="M75 405 H400 V512 H75 Z"/>
      <path d="M75 405 L60 415 V500 L75 512 M400 405 L415 415 V500 L400 512"/>
      <path d="M95 512 V540 H380 V512"/>
    </g>

    <g transform="translate(86 315) rotate(-90)">
      <circle class="brand-dot" cx="-22" cy="-2" r="2"/>
      <text class="brand-name" x="-17" y="0" font-size="5.2">COBALT WREN</text>
      <text class="small-copy" x="3" y="8" font-size="3" text-anchor="middle">Buccal Collection Kit</text>
    </g>
    <g transform="translate(387 315) rotate(90)">
      <circle class="brand-dot" cx="-22" cy="-2" r="2"/>
      <text class="brand-name" x="-17" y="0" font-size="5.2">COBALT WREN</text>
      <text class="small-copy" x="3" y="8" font-size="3" text-anchor="middle">Buccal Collection Kit</text>
    </g>

    <g transform="translate(240 315) rotate(180)">
      <g class="small-copy" font-size="3">
        <text x="-125" y="-38">Made in USA</text>
        <text x="-125" y="-33">Distributed by Cobalt Wren</text>
        <text x="-65" y="-38">Lot / Exp</text>
        <text x="-125" y="-14">Thank you for choosing Cobalt Wren. Your kit contains everything needed to collect a sample</text>
        <text x="-125" y="-9">at home and send it to our lab for analysis. Please read every step before you begin.</text>
        <text x="-125" y="2">Results arrive in your online account within three weeks of the lab receiving your sample.</text>
        <text x="-125" y="7">Your data stays private and is never shared without your consent.</text>
        <text x="-125" y="18">Kit contents: one swab, one tube,</text>
        <text x="-125" y="23">one return envelope.</text>
        <text x="-125" y="34">Keep at room temperature and out of reach of children.</text>
      </g>
    </g>

    <g class="front-brand">
      <circle class="brand-dot" cx="250" cy="439" r="7"/>
      <text class="brand-name" x="250" y="469" font-size="13" text-anchor="middle">COBALT WREN</text>
    </g>
  </g>

  <!-- ================= INNER SIDE ================= -->
  <g class="inner-side">
    <g class="network-accents">
      <path d="M505 330 L540 335 L570 345 L600 370 L505 370 Z" fill="url(#net-band)" role="img" aria-label="Blue and green polygon network in the lower left of the inner panel"/>
      <path d="M505 300 L530 310 L520 330 L505 332 Z" fill="url(#net-band-fade)" role="img" aria-label="Light polygon accent at the left edge"/>
      <path d="M735 265 L820 265 L835 300 L790 290 L750 280 Z" fill="url(#net-band)" role="img" aria-label="Blue and green polygon network in the upper right of the inner panel"/>
      <path d="M500 370 L560 370 L530 395 L500 405 Z" fill="url(#net-band-fade)" role="img" aria-label="Polygon network in the lower left tuck"/>
      <path d="M560 405 L640 405 L700 410 L760 390 L810 372 L835 372 V410 L760 420 L650 425 L560 425 Z" fill="url(#net-band)" role="img" aria-label="Blue and green polygon network along the top of the base panel"/>
      <path d="M770 455 L800 460 L805 500 L780 505 Z" fill="url(#net-band-fade)" role="img" aria-label="Scattered triangles right of the window"/>
    </g>

    <g class="die">
      <path d="M535 88 H815 L835 96 V110 H515 V96 Z"/>
      <rect x="515" y="110" width="320" height="118"/>
      <path d="M492 228 H858 V265 H492 Z"/>
      <path d="M515 228 V265 M835 228 V265"/>
      <rect x="490" y="265" width="370" height="105"/>
      <path d="M515 265 V370 M835 265 V370"/>
      <path d="M490 275 H465 V360 H490"/>
      <path d="M860 275 H885 V360 H860"/>
      <path d="M492 370 H858 V405 H492 Z"/>
      <path d="M515 370 V405 M835 370 V405"/>
      <path d="M515 410 H835 V512 H515 Z"/>
      <path d="M515 410 L500 420 V500 L515 512 M835 410 L850 420 V500 L835 512"/>
      <rect x="565" y="440" width="225" height="55" rx="6"/>
      <path d="M535 512 V540 H815 V512"/>
    </g>

    <g class="instructions">
      <circle class="bullet" cx="544" cy="127" r="2"/>
      <text class="small-copy" font-size="4.4" x="550" y="129">Before starting, <tspan class="strong">register your kit</tspan> at www.wrenkit.com/cobaltwren</text>
      <text class="small-copy strong" font-size="4.4" x="550" y="135">DO NOT <tspan font-weight="400">eat, drink, smoke, chew gum, brush your teeth, or use mouth wash for at least 30 minutes prior to sample</tspan></text>
      <text class="small-copy" font-size="4.4" x="550" y="141">collection; else you risk contaminating your sample.</text>
      <text class="small-copy" font-size="4.4" x="550" y="152">(Notes to designer: please use the same icons included in the box design and include the</text>
      <text class="small-copy" font-size="4.4" x="550" y="158">following bullet points below each icon)</text>

      <rect class="step-art" x="545" y="164" width="50" height="40" role="img" aria-label="Step 1 illustration: hands opening the swab tube"/>
      <rect class="step-art" x="600" y="164" width="50" height="40" role="img" aria-label="Step 2 illustration: swabbing the inside of the cheek"/>
      <rect class="step-art" x="655" y="164" width="50" height="40" role="img" aria-label="Step 3 illustration: breaking the swab into the tube"/>
      <rect class="step-art" x="710" y="164" width="50" height="40" role="img" aria-label="Step 4 illustration: shaking the closed tube"/>
      <rect class="step-art" x="765" y="164" width="50" height="40" role="img" aria-label="Step 5 illustration: tube placed in return envelope"/>

      <g class="small-copy" font-size="3">
        <text x="546" y="210">1. Open the tube and</text><text x="546" y="214">take out the swab.</text>
        <text x="601" y="210">2. Swab inside of each</text><text x="601" y="214">cheek for thirty seconds.</text>
        <text x="656" y="210">3. Break the swab off</text><text x="656" y="214">into the collection tube.</text>
        <text x="711" y="210">4. Close the tube and</text><text x="711" y="214">shake it gently ten times.</text>
        <text x="766" y="210">5. Place the tube in the</text><text x="766" y="214">return envelope and mail.</text>
      </g>
    </g>
  </g>
</svg>
</body>
</html>
```